create a webpage for optometry practice

I'm looking to create a professional and elegant webpage for my practice. I prefer neutral earthy colors, but I am open to other ideas. I have included an image of my logo to be used in the process. This will be a page that will illustrate information about my practice and the kind of services we offer. I am in process of having the practice remodeled. So I don't have any photos of my practice to include yet.

Target Market(s)

My practice serves young and mature families.

Industry/Entity Type

It Professional

Number of Pages Required

5+ page

Font styles to use
Sans Serif

Colors
33a6d7
86cfc6
85cae6
cadf82
3276b5
faa54b
abd036
f78c1e

Requirements
Must have
• I would need to incorporate information about my practice, services, insurance accepted, make appointment, contact us, and about our family.
Nice to have
• I would like to see something fresh, modern, and unique

```html
<!DOCTYPE html>
<html lang="en">
<head>
<meta charset="utf-8">
<title>Lumina Eye Care – Eye Examination</title>
<link rel="stylesheet" href="https://fonts.googleapis.com/css2?family=Open+Sans:wght@300;400;600;700&display=swap">
<style>
  :root {
    --lime: #abd036;
    --sky: #33a6d7;
    --ink: #111111;
    --text: #333333;
    --paper: #ffffff;
    --mist: #f8f8f8;
    --slate: #808080;
    --brand-teal: #2a9fb3;
  }
  * { box-sizing: border-box; margin: 0; padding: 0; }
  html, body { width: 1200px; height: 1035px; overflow: hidden; }
  body {
    position: relative;
    background: var(--mist);
    font-family: "Open Sans", Arial, sans-serif;
    color: var(--text);
  }
  .abs { position: absolute; }

  .top-rule { left: 0; top: 0; width: 1200px; height: 5px; background: var(--lime); }
  .site-header { left: 0; top: 5px; width: 1200px; height: 102px; background: var(--paper); }
  .brand { left: 78px; top: 38px; display: flex; align-items: center; gap: 10px; }
  .brand-dot { width: 22px; height: 22px; border-radius: 50%; background: var(--lime); }
  .brand-name { font-size: 26px; font-weight: 600; color: var(--brand-teal); letter-spacing: 0.5px; }

  .header-social { left: 1032px; top: 39px; display: flex; gap: 5px; }
  .header-social span { display: block; width: 32px; height: 31px; background: var(--sky); }

  .main-nav { left: 0; top: 107px; width: 1200px; height: 51px; background: var(--sky); }
  .nav-item {
    position: absolute; top: 0; line-height: 51px; transform: translateX(-50%);
    font-size: 22px; font-weight: 600; color: var(--paper); white-space: nowrap;
  }
  .nav-item.is-active { color: var(--ink); }
  .nav-marker { left: 426px; top: 147px; width: 0; height: 0;
    border-left: 11px solid transparent; border-right: 11px solid transparent;
    border-bottom: 11px solid var(--lime); }

  .page-banner { left: 0; top: 158px; width: 1200px; height: 67px; background: var(--lime); }
  .page-title { left: 75px; top: 0; line-height: 67px; font-size: 25px; font-weight: 700; color: var(--paper); }

  .service-photo { left: 29px; top: 270px; width: 543px; height: 363px;
    background: linear-gradient(120deg, #e9e6e2 0%, #c9c4bd 45%, #8d8a86 75%, #5b4a48 100%); }
  .service-heading { left: 589px; top: 264px; font-size: 25px; font-weight: 700; color: var(--ink); }
  .service-copy { left: 589px; top: 318px; width: 572px; font-size: 18px; line-height: 18.8px;
    font-weight: 300; color: var(--text); }
  .btn-appointment { left: 587px; top: 534px; width: 221px; height: 59px;
    border: 1.5px solid var(--sky); color: var(--sky); font-size: 15.5px; font-weight: 600;
    display: flex; align-items: center; justify-content: center; }

  .cta-band { left: 0; top: 687px; width: 1200px; height: 103px; background: var(--sky);
    box-shadow: 0 3px 5px rgba(0,0,0,0.2); }
  .cta-text { left: 120px; top: 0; line-height: 100px; font-size: 18px; font-weight: 600; color: var(--ink); }
  .btn-contact { left: 897px; top: 25px; width: 194px; height: 52px; border: 1.5px solid var(--paper);
    color: var(--paper); font-size: 18px; font-weight: 600;
    display: flex; align-items: center; justify-content: center; }

  .footer-heading { top: 820px; font-size: 19px; font-weight: 700; color: var(--ink); }
  .footer-text { font-size: 16px; line-height: 21px; font-weight: 300; color: var(--text); }
  .about-text { left: 120px; top: 866px; width: 245px; }
  .gallery-thumb { width: 77px; height: 43px; background: var(--slate); }
  .social-tile { left: 639px; width: 31px; height: 31px; background: var(--sky); }
</style>
</head>
<body>
  <div class="abs top-rule"></div>
  <header class="abs site-header"></header>
  <div class="abs brand">
    <span class="brand-dot"></span>
    <span class="brand-name">LUMINA EYE CARE</span>
  </div>
  <div class="abs header-social" aria-label="Social links">
    <span></span><span></span><span></span>
  </div>

  <nav class="abs main-nav">
    <span class="nav-item" style="left:273px">HOME</span>
    <span class="nav-item is-active" style="left:437px">SERVICES</span>
    <span class="nav-item" style="left:600px">GALLERY</span>
    <span class="nav-item" style="left:760px">NEWS</span>
    <span class="nav-item" style="left:908px">ABOUT US</span>
    <span class="nav-item" style="left:1080px">CONTACT</span>
  </nav>
  <div class="abs nav-marker"></div>

  <section class="abs page-banner">
    <h1 class="abs page-title">EYE EXAMINATION</h1>
  </section>

  <div class="abs service-photo" role="img" aria-label="Optometrist examining a patient's eyes with a slit lamp"></div>
  <h2 class="abs service-heading">Comprehensive Eye examination</h2>
  <p class="abs service-copy">Lorem ipsum dolor sit amet, consectetur adipiscing elit. Pellentesque quis eros lobortis, vestibulum turpis ac, pulvinar odio. Praesent vulputate a elit ac mollis. In sit amet ipsum turpis. Pellentesque venenatis, libero vel euismod lobortis, mi metus luctus augue, eget dapibus elit nisi eu massa. Phasellus sollicitudin nisl posuere nibh ultricies, et fringilla dui gravida. Donec iaculis adipiscing neque, non congue massa euismod quis. Etiam interdum dolor sit amet justo vulputate, non mollis velit venenatis.</p>
  <div class="abs btn-appointment">MAKE AN APPOINTMENT</div>

  <section class="abs cta-band">
    <p class="abs cta-text">GET IN TOUCH TO JOIN OUR COMMUNITY</p>
    <div class="abs btn-contact">CONTACT US</div>
  </section>

  <footer>
    <h3 class="abs footer-heading" style="left:120px">ABOUT US</h3>
    <p class="abs footer-text about-text">Dr Harlow is an expert in minimally invasive approaches to treat spine and joint pain as well as neck, back, and joint injuries.</p>

    <h3 class="abs footer-heading" style="left:380px">PHOTO GALLERY</h3>
    <div class="abs gallery-thumb" style="left:383px;top:864px"></div>
    <div class="abs gallery-thumb" style="left:468px;top:864px"></div>
    <div class="abs gallery-thumb" style="left:383px;top:918px"></div>
    <div class="abs gallery-thumb" style="left:468px;top:918px"></div>

    <h3 class="abs footer-heading" style="left:638px">SOCIAL NETWORK</h3>
    <div class="abs social-tile" style="top:852px"></div>
    <div class="abs social-tile" style="top:890px"></div>
    <div class="abs social-tile" style="top:928px"></div>

    <h3 class="abs footer-heading" style="left:859px">CONTACT INFO</h3>
    <p class="abs footer-text" style="left:859px;top:866px">OPTOMETRY</p>
    <p class="abs footer-text" style="left:859px;top:908px">Call us toll free:&nbsp; (555) 014-2777<br>1-800-555-0199&nbsp; (800-555-0199)</p>
  </footer>
</body>
</html>
```